Lantern Ridge Treks Flyer

I have an adventure travel company and I need a flyer to promote my trip to Ukraine.
I would like to have a universal flyer that I can change based on the trip.
The Title should say "Travel to Ukraine: 9 Day Eastern European Adventure"
The date should be under the title.
The background photo should be kiev2.jpg
The highlights of the trip, then price $1200 and what it includes. See the text for highlights and includes sections here:
http://www.lanternridgetreks.com/#!featured-trip
The website link (www.lanternridgetreks.com) should be somewhere in the bottom.
You can use other photos provided or from my website that relates to Ukraine trip.
Travel

```html
<!DOCTYPE html>
<html lang="en">
<head>
<meta charset="utf-8">
<title>Lantern Ridge Treks – Travel to Ukraine</title>
<link rel="stylesheet" href="https://fonts.googleapis.com/css2?family=Bevan&family=PT+Sans:wght@400;700&display=swap">
<style>
  :root {
    --red: #e21b25;
    --red-deep: #b5121b;
    --yellow: #ffe81a;
    --white: #ffffff;
    --sky: #1ea5e0;
    --sky-deep: #0d83c3;
    --frame: #ffffff;
  }
  * { box-sizing: border-box; margin: 0; padding: 0; }
  html, body { width: 926px; height: 1200px; overflow: hidden; background: #fff; }
  .flyer {
    position: relative; width: 926px; height: 1200px; overflow: hidden;
    background: linear-gradient(180deg, var(--red) 0%, var(--red) 70%, var(--red-deep) 100%);
    font-family: "PT Sans", Arial, sans-serif; color: var(--white);
  }
  .hero-photo {
    position: absolute; left: 0; top: 170px; width: 926px; height: 582px;
    background: linear-gradient(180deg, #5c7f8f 0%, #7a98a0 18%, #4f6b3c 32%, #c9a640 55%, #7a5a48 75%, #8d7d70 100%);
    clip-path: polygon(0 14%, 100% 0, 100% 100%, 0 100%);
  }
  .snapshot {
    position: absolute; border: 5px solid var(--frame);
    box-shadow: 0 3px 8px rgba(0,0,0,.45);
  }
  .snapshot--lavra { left: 6px; top: -6px; width: 168px; height: 124px; transform: rotate(-5deg);
    background: linear-gradient(180deg, #9fb9cf, #cdb45a 55%, #6e7d55); }
  .snapshot--cave { left: 712px; top: 82px; width: 198px; height: 148px; transform: rotate(5deg);
    background: radial-gradient(ellipse at 55% 45%, #d8bfa0, #8a6a4e 55%, #3e2c20); }
  .title-block {
    position: absolute; left: 34px; top: 170px; width: 860px;
    transform: rotate(-10deg); transform-origin: left top;
  }
  .title {
    font-family: "Bevan", Georgia, serif; color: var(--yellow);
    font-size: 43px; line-height: 1.02; font-weight: 400;
    text-shadow: 2px 2px 0 rgba(120,0,0,.35);
  }
  .title span { display: block; }
  .title span + span { padding-left: 145px; }
  .dates {
    margin: 6px 0 0 270px; font-family: "PT Sans", Arial, sans-serif;
    font-weight: 700; font-size: 22px; color: var(--white);
  }
  .price-badge {
    position: absolute; left: 44px; top: 246px; width: 132px; height: 132px;
    border-radius: 50%; background: var(--yellow); border: 5px solid var(--red);
    box-shadow: 0 0 0 2px var(--yellow);
    display: flex; flex-direction: column; align-items: center; justify-content: center;
    transform: rotate(-10deg); font-family: "Bevan", Georgia, serif; color: var(--red);
  }
  .price-badge .label { font-size: 21px; line-height: 1; }
  .price-badge .amount { font-size: 30px; line-height: 1.1; }
  .accent-stripe {
    position: absolute; left: 0; top: 740px; width: 926px; height: 12px; background: var(--sky);
  }
  .gallery .snapshot { top: 657px; height: 138px; }
  .snapshot--tram { left: 57px; width: 208px; background: linear-gradient(180deg, #b9c3c0, #8f8f7f 50%, #5a5650); }
  .snapshot--peak { left: 372px; width: 179px; background: linear-gradient(180deg, #8da6b4, #c9d2d4 45%, #6d7a62); }
  .snapshot--coast { left: 658px; width: 197px; background: linear-gradient(180deg, #4f7899, #3f6a8a 45%, #5c7a3c); }
  .section { position: absolute; left: 30px; width: 880px; }
  .section--highlights { top: 802px; }
  .section--included { top: 998px; }
  .section-heading {
    font-family: "Bevan", Georgia, serif; color: var(--yellow);
    font-size: 28px; letter-spacing: .5px; line-height: 1.15; margin-bottom: 4px;
  }
  .checklist { list-style: none; font-size: 15.5px; line-height: 24.5px; }
  .checklist li { position: relative; padding-left: 20px; }
  .checklist li::before {
    content: ""; position: absolute; left: 4px; top: 7px; width: 5px; height: 10px;
    border: solid var(--yellow); border-width: 0 2px 2px 0; transform: rotate(40deg);
  }
  .key { color: var(--yellow); }
  .inclusions { list-style: none; font-size: 15.5px; line-height: 24px; padding-left: 18px; }
  .inclusions li::before { content: "• "; color: var(--yellow); font-weight: 700; }
  .footer {
    position: absolute; left: 0; top: 1136px; width: 926px; height: 64px;
    background: linear-gradient(180deg, var(--sky), var(--sky-deep));
    display: flex; align-items: center; justify-content: space-between; padding: 0 12px;
  }
  .contact { font-size: 11.5px; line-height: 14px; font-weight: 700; color: var(--white); }
  .contact .name { color: var(--yellow); }
  .contact .email { color: var(--yellow); }
  .website { font-family: "Bevan", Georgia, serif; color: var(--yellow); font-size: 19px; margin-left: 40px; }
  .phone { font-family: "Bevan", Georgia, serif; color: var(--yellow); font-size: 27px; }
</style>
</head>
<body>
<main class="flyer">
  <div class="hero-photo" role="img" aria-label="Aerial view of the Kiev Pechersk Lavra with golden domes above the Dnieper River"></div>

  <div class="snapshot snapshot--lavra" role="img" aria-label="Golden-domed cathedral in Kiev"></div>
  <div class="snapshot snapshot--cave" role="img" aria-label="Crystal formations inside a Crimean cave"></div>

  <header class="title-block">
    <h1 class="title"><span>Travel to Ukraine: 9 Day Eastern</span><span>European Adventure</span></h1>
    <p class="dates">Fri May 18 - Sun May 27</p>
  </header>

  <div class="price-badge"><span class="label">PRICE</span><span class="amount">$1200</span></div>

  <div class="accent-stripe"></div>
  <div class="gallery">
    <div class="snapshot snapshot--tram" role="img" aria-label="Red tram on a tree-lined Odessa street"></div>
    <div class="snapshot snapshot--peak" role="img" aria-label="Pine tree on a rocky mountain peak in Crimea"></div>
    <div class="snapshot snapshot--coast" role="img" aria-label="Yalta coastline along the Black Sea"></div>
  </div>

  <section class="section section--highlights">
    <h2 class="section-heading">HIGHLIGHTS:</h2>
    <ul class="checklist">
      <li>Discover <span class="key">Kiev</span>- the birthplace of Eastern Slavic Civilization</li>
      <li>Meet <span class="key">Crimea's</span> fascinating <span class="key">Tatar</span> Minority in Bakhchysaray - former capital of Crimean Tatar Khans</li>
      <li>Walk to <span class="key">Chufut-Kale</span> - Crimea's best preserved &nbsp;medieval cave town</li>
      <li><span class="key">Hike</span> in the most spectacular areas in Karabi and &nbsp;with a group of professional speleologist</li>
      <li>Inhale the magic <span class="key">Yalta's air</span>- an invigorating blend of sea and pine forest sprinkled with mountain chill</li>
      <li>Visit <span class="key">Odessa</span>- "the Pearl by the Black Sea", Catacombs, Opera house, the factory of sparkling wines and famous <span class="key">Potemkin Steps</span></li>
    </ul>
  </section>

  <section class="section section--included">
    <h2 class="section-heading">INCLUDED:</h2>
    <ul class="inclusions">
      <li>9 nights accommodations</li>
      <li>Breakfast, lunch and dinner daily</li>
      <li>English speaking guides at every destination.</li>
      <li>All Local Transfers (trains, buses and vans), &nbsp;sightseeing tours and entrance fees</li>
    </ul>
  </section>

  <footer class="footer">
    <address class="contact" style="font-style:normal">
      <div class="name">Marta Levchenko</div>
      <div>Fax # 718-555-0142</div>
      <div>Email &nbsp;<span class="email">marta@lanternridgetreks.com</span></div>
    </address>
    <div class="website">www.lanternridgetreks.com</div>
    <div class="phone">1.718.555.0142</div>
  </footer>
</main>
</body>
</html>
```